female esthetician looking for an impact business card

I an an expert in skin care industry with high experience in NYC.I want my business card to look professional , an impact at first look. I do want a combination between white and gold . I believe the font will be great if is gold.. The Fonts are also important. MARISELA VONDRAKE (SKIN CARE BOUTIQUE)

THIS SHOULD BE THE BUSINESS NAME, and should be placed on th eback of the card.
IN front m, the name MARISELA VONDRAKE - ESTHETCIAN

BY APPOINTMENTS ONLY: 555.218.9031

Target Market(s)

HIGH END CLIENTELE

Contact Information for Business Card

iT WILL BE on a luxury paper. I neeed the wow feeling

Requirements
Should not have
• pictures

```html
<!DOCTYPE html>
<html lang="en">
<head>
<meta charset="utf-8">
<title>Marisela Vondrake – Business Card</title>
<link rel="stylesheet" href="https://fonts.googleapis.com/css2?family=Cinzel:wght@400;500&display=swap">
<style>
  :root {
    --backdrop: #dddddd;
    --paper: #ffffff;
    --gold: #d4a262;
    --gold-card: #d9ae7f;
    --ink-light: #ffffff;
  }
  html, body {
    margin: 0;
    padding: 0;
    width: 1200px;
    height: 897px;
    overflow: hidden;
    background: var(--backdrop);
  }
  .canvas {
    position: relative;
    width: 1200px;
    height: 897px;
    font-family: "Cinzel", "Times New Roman", serif;
  }
  .card {
    position: absolute;
    left: 329px;
    width: 543px;
    height: 310px;
  }
  .card--front { top: 108px; background: var(--paper); color: var(--gold); }
  .card--back { top: 479px; background: var(--gold-card); color: var(--ink-light); }

  .front-block {
    position: absolute;
    left: 0;
    right: 0;
    top: 78px;
    text-align: center;
  }
  .holder-name {
    margin: 0;
    font-size: 18px;
    font-weight: 500;
    letter-spacing: 1.6px;
    line-height: 22px;
  }
  .holder-title {
    margin: 0;
    font-size: 12.5px;
    letter-spacing: 0.8px;
    line-height: 18px;
  }
  .divider {
    width: 187px;
    height: 1px;
    margin: 11px auto 10px;
    background: var(--gold);
  }
  .contact {
    margin: 0;
    font-size: 13px;
    line-height: 19px;
    letter-spacing: 0.6px;
  }
  .contact--phone { font-size: 13.5px; line-height: 20px; letter-spacing: 0.4px; }
  .contact--address { margin-top: 8px; font-size: 13.5px; letter-spacing: 0.8px; }

  .back-block {
    position: absolute;
    left: 0;
    right: 0;
    top: 128px;
    text-align: center;
  }
  .brand-name {
    margin: 0;
    font-size: 32px;
    font-weight: 500;
    letter-spacing: 1px;
    line-height: 36px;
  }
  .brand-tagline {
    margin: 6px 0 0;
    font-size: 13px;
    letter-spacing: 3px;
    line-height: 18px;
  }
</style>
</head>
<body>
<main class="canvas">
  <section class="card card--front" aria-label="Card front">
    <div class="front-block">
      <h1 class="holder-name">MARISELA VONDRAKE</h1>
      <p class="holder-title">Esthetician</p>
      <div class="divider"></div>
      <p class="contact contact--phone">By appointments only: 555.218.9031</p>
      <p class="contact">INFO@VONDRAKESKIN.COM</p>
      <p class="contact">WWW.VONDRAKESKIN.COM</p>
      <p class="contact contact--address">412b Alder Lane, Riverton, NZ. 8042</p>
    </div>
  </section>
  <section class="card card--back" aria-label="Card back">
    <div class="back-block">
      <h2 class="brand-name">MARISELA VONDRAKE</h2>
      <p class="brand-tagline">SKIN CARE BOUTIQUE</p>
    </div>
  </section>
</main>
</body>
</html>
```